Candle Rental Business seeks new website design

We need a new website design for a Candle hire business. The business rents out pillar candles for events such as weddings and corporate events. Our main target market is weddings. The business name is Hire a Lantern. The business name does not have a logo design.

We would like a website that is light in colours and creates a warm atmosphere. The design needs to be elegant and upmarket. There are different size candles that we hire out, ranging from 10cm diameter to 20cm diameter, flat, tall etc. All our candles are white in colour. Its just the size that differs.

We would also like to include a section for hiring out decor such as glassvases, candlebras, overlays and chairs sachets, chair covers. However, this is not the businesses main focus but an additional offering to customers.

Target Market(s)

Wedding venues and brides. Corporate events. School dances.

Industry/Entity Type

Hospitality

Logo Text

Hire a Lantern

Number of Pages Required

1 page

Font styles to use
Sans Serif
Script

Requirements
Must have
• Pictures of pillar candles. Plain white candles. The website must centre around candles.
Nice to have
• Different examples of candle centrepieces
Should not have
• Pictures must not be of brides. Pictures of surrounding is perferable.

```html
<!DOCTYPE html>
<html lang="en">
<head>
<meta charset="utf-8">
<title>Hire a Lantern</title>
<link rel="stylesheet" href="https://fonts.googleapis.com/css2?family=Tinos:wght@400;700&family=Open+Sans:wght@400&display=swap">
<style>
:root{
  --page:#2d2d2d;
  --panel:#262626;
  --panel-dark:#1b1b1b;
  --cream-top:#ecdcbb;
  --cream-bottom:#e9d2a6;
  --ink:#4a4440;
  --gold:#e8cfa0;
  --muted:#a9a9a9;
  --soft:#8f8f8f;
  --white:#ffffff;
}
*{box-sizing:border-box;margin:0;padding:0}
html,body{width:1200px;height:1189px;overflow:hidden;background:var(--page)}
body{font-family:"Tinos",serif;position:relative}
.site{position:absolute;left:132px;top:0;width:936px}
.masthead{height:144px;background:linear-gradient(var(--cream-top),var(--cream-bottom));position:relative}
.brand{position:absolute;top:22px;left:0;right:0;text-align:center;font-family:"Tinos",serif;font-weight:700;font-size:41px;letter-spacing:1px;color:var(--ink)}
.brand-rule{position:absolute;top:76px;left:0;right:0;height:1px;background:#b9a78a}
.brand-mark{position:absolute;top:73px;left:447px;width:44px;height:4px;background:var(--white)}
.main-nav{position:absolute;top:102px;left:0;right:0;display:flex;justify-content:center;gap:31px;font-size:13px;color:var(--ink)}
.main-nav a{color:inherit;text-decoration:none}
.main-nav .current{text-decoration:underline}
.main-nav .current::before{content:"•";margin-right:6px;font-size:10px}
.hero{height:369px;background:radial-gradient(ellipse at 50% 45%,#e9a65a 0%,#a8502a 28%,#5a1f12 60%,#2a0c07 100%);position:relative}
.hero-arrow{position:absolute;top:172px;width:14px;height:24px}
.hero-arrow.prev{left:22px}
.hero-arrow.next{right:22px}
.welcome{height:293px;background:var(--panel);text-align:center;padding-top:31px}
.welcome h1{display:inline-block;font-weight:400;font-size:34px;color:var(--gold);padding-bottom:2px;border-bottom:3px solid var(--gold);line-height:1.1}
.welcome h2{font-weight:400;font-size:16px;color:var(--white);margin-top:22px}
.welcome p{font-family:"Open Sans",sans-serif;font-size:10.4px;line-height:21px;color:var(--muted);margin:12px 28px 0}
.btn{display:inline-block;margin-top:27px;width:108px;height:45px;line-height:43px;border:1px solid #cfcfcf;color:var(--gold);font-size:15.5px;text-decoration:none}
.feature-row{display:flex;height:280px}
.gallery-tile{width:468px;position:relative;background:radial-gradient(ellipse at 30% 45%,#f6d9a8 0%,#d4502e 22%,#a8141c 55%,#6a0b12 100%)}
.gallery-tile .title{position:absolute;right:22px;top:114px;font-size:27px;color:var(--gold)}
.gallery-tile .more{position:absolute;right:22px;top:160px;font-size:14px;color:var(--white);display:flex;align-items:center;gap:5px}
.services{width:468px;background:var(--panel-dark);padding:28px 30px 0 43px}
.services h2{font-weight:400;font-size:27px;color:var(--gold)}
.services p{font-family:"Open Sans",sans-serif;font-size:10.4px;line-height:19.2px;color:var(--muted);margin-top:13px;text-align:justify}
.service-list{list-style:none;display:grid;grid-template-columns:176px 1fr;row-gap:12px;margin-top:15px;font-size:15.2px;color:var(--soft)}
.service-list li{display:flex;align-items:center;gap:9px}
.service-list li.active{color:var(--white)}
.site-footer{position:absolute;top:1106px;left:133px;width:935px}
.footer-nav{font-size:11.5px;color:var(--soft)}
.footer-nav span{margin:0 8px;color:#666}
.copyright{font-size:11.5px;color:var(--soft);margin-top:13px}
.social{position:absolute;right:1px;top:17px;display:flex;gap:7px}
.social span{width:26px;height:26px;border-radius:50%;background:#5a5a5a}
</style>
</head>
<body>
<div class="site">
  <header class="masthead">
    <div class="brand">HIRE A LANTERN</div>
    <div class="brand-rule"></div>
    <div class="brand-mark"></div>
    <nav class="main-nav">
      <a class="current" href="#">HOME</a>
      <a href="#">ORDER NOW</a>
      <a href="#">ABOUT US</a>
      <a href="#">GALLERY</a>
      <a href="#">CONTACT US</a>
    </nav>
  </header>
  <section class="hero" role="img" aria-label="Rows of lit white pillar candles glowing in a brick fireplace">
    <svg class="hero-arrow prev" viewBox="0 0 14 24"><path d="M12 1 2 12l10 11" fill="none" stroke="#7a5040" stroke-width="2"/></svg>
    <svg class="hero-arrow next" viewBox="0 0 14 24"><path d="M2 1l10 11L2 23" fill="none" stroke="#7a5040" stroke-width="2"/></svg>
  </section>
  <section class="welcome">
    <h1>WELCOME</h1>
    <h2>Donec turpis magna, luctus vel ipsum et, egestas sollicitudin odio</h2>
    <p>Aliquam ullamcorper diam sit amet hendrerit feugiat. Interdum et malesuada fames ac ante ipsum primis in faucibus. Lorem ipsum dolor sit amet, consectetur adipiscing elit. Donec nec ipsum ut neque malesuada eleifend. Nam fringilla ligula varius, maximus mauris in, bibendum arcu. Phasellus nec ante in justo tempor malesuada. Class aptent taciti sociosqu ad litora torquent per conubia nostra, per inceptos himenaeos. Pellentesque consectetur vulputate finibus. Integer vel nunc eget elit placerat malesuada.</p>
    <a class="btn" href="#">Order Now</a>
  </section>
  <section class="feature-row">
    <div class="gallery-tile" role="img" aria-label="Two white candles glowing against a red backdrop">
      <div class="title">Candles Gallery</div>
      <div class="more"><svg width="10" height="10" viewBox="0 0 10 10"><circle cx="5" cy="5" r="4.2" fill="none" stroke="#fff" stroke-width="1.4"/><path d="M3 5h4M5.2 3.3 7 5 5.2 6.7" fill="none" stroke="#fff" stroke-width="1.2"/></svg>View All</div>
    </div>
    <div class="services">
      <h2>Our Services</h2>
      <p>Aliquam ullamcorper diam sit amet hendrerit feugiat. Interdum et malesuada fames ac ante ipsum primis in faucibus. Lorem ipsum dolor sit amet, consectetur adipiscing elit. Donec nec ipsum ut neque malesuada eleifend. Nam fringilla ligula varius, maximus mauris in, bibendum arcu.</p>
      <ul class="service-list">
        <li class="active"><svg width="11" height="11" viewBox="0 0 10 10"><circle cx="5" cy="5" r="4.2" fill="none" stroke="currentColor" stroke-width="1.4"/><path d="M3 5h4M5.2 3.3 7 5 5.2 6.7" fill="none" stroke="currentColor" stroke-width="1.2"/></svg>Pillar Candles</li>
        <li><svg width="11" height="11" viewBox="0 0 10 10"><circle cx="5" cy="5" r="4.2" fill="none" stroke="currentColor" stroke-width="1.4"/><path d="M3 5h4M5.2 3.3 7 5 5.2 6.7" fill="none" stroke="currentColor" stroke-width="1.2"/></svg>Overlays and Chairs Sachets</li>
        <li><svg width="11" height="11" viewBox="0 0 10 10"><circle cx="5" cy="5" r="4.2" fill="none" stroke="currentColor" stroke-width="1.4"/><path d="M3 5h4M5.2 3.3 7 5 5.2 6.7" fill="none" stroke="currentColor" stroke-width="1.2"/></svg>Glassvases</li>
        <li><svg width="11" height="11" viewBox="0 0 10 10"><circle cx="5" cy="5" r="4.2" fill="none" stroke="currentColor" stroke-width="1.4"/><path d="M3 5h4M5.2 3.3 7 5 5.2 6.7" fill="none" stroke="currentColor" stroke-width="1.2"/></svg>Chair Covers</li>
        <li><svg width="11" height="11" viewBox="0 0 10 10"><circle cx="5" cy="5" r="4.2" fill="none" stroke="currentColor" stroke-width="1.4"/><path d="M3 5h4M5.2 3.3 7 5 5.2 6.7" fill="none" stroke="currentColor" stroke-width="1.2"/></svg>Candlebras</li>
      </ul>
    </div>
  </section>
</div>
<footer class="site-footer">
  <div class="footer-nav">Home<span>|</span>Order Now<span>|</span>About us<span>|</span>Gallery<span>|</span>Contact us</div>
  <div class="copyright">Copyright &nbsp;© &nbsp;2016 &nbsp; Hire a Lantern. &nbsp; All rights reserved.</div>
  <div class="social" aria-label="Social links"><span></span><span></span><span></span><span></span></div>
</footer>
</body>
</html>
```